Flyer Required for Economics Tuition business in Singapore

Require a 4-page, A4 bi-fold full colour flyer. To use attractive & vibrant colours. Can make use of colour schemes and design layouts from upcoming website revamp: http://lessonmaple.com/Website/
Target audience for the flyer will be 17 - 18 years old A Level students in Singapore studying in Junior Colleges.
I have attached the detailed design brief with the content required for the flyer as a file titled "Design Brief.docx" & also the logo for our business to be used in the flyer & optional photos that can be used in the flyer

```html
<!DOCTYPE html>
<html lang="en">
<head>
<meta charset="utf-8">
<title>LessonMaple Economics Flyer</title>
<link href="https://fonts.googleapis.com/css2?family=Open+Sans:wght@400;600;700&display=swap" rel="stylesheet">
<style>
:root{
  --orange:#f39200;
  --orange-dark:#e07b00;
  --charcoal:#3a3a3a;
  --ink:#333;
  --muted:#666;
  --stage:#4a4a4a;
  --stage-top:#6b6b6b;
  --paper:#fff;
  --paper-warm:#fdf6ec;
  --photo-blue:#8fa6bb;
  --photo-deep:#4f6479;
}
*{box-sizing:border-box;margin:0;padding:0}
html,body{width:1200px;height:1000px;overflow:hidden}
body{font-family:"Open Sans",Arial,sans-serif;color:var(--ink);
  background:linear-gradient(180deg,#1e1e1e 0,#1e1e1e 42px,var(--stage-top) 42px,var(--stage) 520px,#3d3d3d 955px,#1e1e1e 955px);position:relative}
.page{position:absolute;width:278px;height:393px;background:linear-gradient(180deg,var(--paper) 60%,var(--paper-warm));box-shadow:0 4px 12px rgba(0,0,0,.45);overflow:hidden}
.p1{left:282px;top:95px}.p2{left:585px;top:95px}.p3{left:282px;top:517px}.p4{left:585px;top:517px}
.abs{position:absolute}
.body-text{font-size:3.6px;line-height:4.6px;color:var(--ink)}
.body-text p{margin-bottom:2.5px}
.h-orange{font-size:5.4px;font-weight:700;color:var(--orange);line-height:6px}
.photo{background:linear-gradient(160deg,var(--photo-blue),var(--photo-deep))}
.photo-warm{background:linear-gradient(160deg,#d9a46b,#7a5a3c)}
.photo-grey{background:linear-gradient(160deg,#cfd3d6,#8d949a)}

/* page 1 */
.header-band{left:0;top:0;width:278px;height:62px}
.brand{left:10px;top:22px;display:flex;align-items:center;gap:4px}
.brand-dot{width:9px;height:9px;border-radius:50%;background:var(--orange)}
.brand-name{font-size:10px;font-weight:700;color:var(--orange)}
.headline{left:108px;top:10px;width:170px;text-align:center;color:#fff}
.headline h1{font-size:14.5px;font-weight:700;line-height:17px}
.headline p{font-size:6.6px;line-height:8px}
.congrats{left:14px;top:156px;width:250px;height:9px;background:#d9d9d9}
.congrats span{position:absolute;left:68px;top:-1px;height:11px;width:120px;background:var(--charcoal);color:#fff;font-size:4.6px;line-height:11px;text-align:center}
.congrats b{color:var(--orange)}
.results{left:16px;top:169px;width:246px;border-collapse:collapse;table-layout:fixed;font-size:3px;line-height:5.6px}
.results td{border:.3px solid #888;height:6.1px;padding:0 1.5px;white-space:nowrap;overflow:hidden}
.results td.g{color:var(--orange-dark)}
.testi-tab{left:178px;top:323px;width:90px;height:14px;background:var(--charcoal);color:#fff;font-size:5px;line-height:14px;text-align:center}
.orange-band{left:0;top:337px;width:278px;height:56px;background:var(--orange)}
.band-quote{top:342px;width:118px;font-size:3.2px;line-height:4.1px;color:#fff}
.band-quote p{margin-bottom:3px}
.tag{font-size:3.3px;line-height:5px;background:#fff;color:var(--ink);padding:0 3px;border:.5px solid var(--orange);display:inline-block}
.tag b{color:var(--orange-dark);font-weight:700}

/* page 2 */
.founder-label{left:70px;top:97px;width:140px;height:14px;background:#eef2f5;border:.6px solid var(--charcoal);font-size:6.6px;line-height:13px;text-align:center}
.founder-label b{color:var(--orange);font-weight:700}
.sec-head{left:14px;height:8px;padding:0 3px;background:var(--orange);color:#fff;font-size:5.2px;line-height:8px;font-weight:600}
.sec-rule{left:14px;height:.6px;background:var(--orange)}

/* page 3 */
.testi-label{left:88px;top:12px;width:104px;height:10px;background:rgba(255,255,255,.85);font-size:5.6px;line-height:10px;text-align:center}
.testi-label b{color:var(--orange);font-weight:600}
.tcol{top:124px;width:120px;font-size:3.2px;line-height:4.1px}
.tcol p{margin-bottom:1.5px}
.tcol .tag{margin-bottom:4px}

/* page 4 */
.sched-label,.fees-label{height:9px;background:var(--charcoal);color:#fff;font-size:5px;line-height:9px;text-align:center}
.schedule{top:117px;width:118px;border-collapse:collapse;font-size:3.5px}
.schedule td{border:.4px solid #555;height:7px;padding:0 1.5px;white-space:nowrap}
.loc-bar{left:70px;top:200px;width:140px;height:11px;background:var(--orange);color:#fff;font-size:6px;line-height:11px;text-align:center;font-weight:600}
.loc-box{left:40px;top:213px;width:200px;height:78px;border:.6px solid var(--orange);background:#fff}
.loc{font-size:3.5px;line-height:4.4px;width:90px}
.loc h3{font-size:4.6px;color:var(--orange);font-weight:700;line-height:6px}
.fees{left:0;top:320px;width:278px;text-align:center;font-size:4.6px;line-height:5.6px}
.contact{left:76px;top:352px;width:126px;height:24px;border:.6px solid var(--orange);text-align:center;font-size:5px;line-height:6.6px;padding-top:4px;background:#fff}
.contact b{color:var(--orange)}
</style>
</head>
<body>

<section class="page p1">
  <svg class="abs header-band" width="278" height="62" viewBox="0 0 278 62">
    <rect width="278" height="62" fill="#3a3a3a"/>
    <polygon points="100,0 278,0 278,62 88,62" fill="#f39200"/>
  </svg>
  <div class="abs brand"><span class="brand-dot"></span><span class="brand-name">LessonMaple</span></div>
  <div class="abs headline">
    <h1>Failing Economics?</h1>
    <p>It's time to get the RIGHT help<br>for your A Level Economics!</p>
  </div>

  <div class="abs body-text" style="left:14px;top:68px;width:118px">
    <div class="h-orange">Singapore's Leading Economics<br>Tuition Programme</div>
    <p>The Economics at LessonMaple programme is a structured two year Economics tuition programme designed with the objective of equipping students with the relevant skills to tackle the A Level examinations. Strong emphasis is placed on developing the right thought process in breaking down essay questions &amp; essential case study skills.</p>
    <p>All classes are taught by Mr Adrian Koh, the founder of the programme, who is also the Managing Director for Brightway Education Centre &amp; Clearpath Learning Centre.</p>
  </div>
  <div class="abs body-text" style="left:146px;top:68px;width:118px">
    <div class="h-orange">Why join us?</div>
    <p>Since 2007, Mr Koh has been teaching an average of 150-200 students each year. It is undoubtedly the most attended Economics tuition programme taught by a single tutor in Singapore!</p>
    <p>For the latest A Level results released on 2nd March 2015, More than 95% of our students scored either an A or B for their Economics (on top of that the ratio of As to Bs was 7:1!)</p>
  </div>

  <div class="abs congrats"><span><b>Congratulations</b> to the following students!</span></div>

  <table class="abs results">
    <tr><td>Alyssa Tan</td><td>NVJC</td><td class="g">A</td><td>Bryan Lee</td><td>EGI</td><td class="g">A</td><td>Clara Ng</td><td>SBJC</td><td class="g">A</td></tr>
    <tr><td>Daniel Ong</td><td>RSHS</td><td class="g">A</td><td>Elaine Goh</td><td>HVJC</td><td class="g">A</td><td>Felix Chua</td><td>NVJC</td><td class="g">A</td></tr>
    <tr><td>Grace Lim</td><td>LSJC</td><td class="g">A</td><td>Henry Teo</td><td>EGI</td><td class="g">A</td><td>Irene Yeo</td><td>RSHS</td><td class="g">A</td></tr>
    <tr><td>Jason Koh</td><td>SBJC</td><td class="g">A</td><td>Karen Sim</td><td>NVJC</td><td class="g">A</td><td>Leon Tay</td><td>EGI</td><td class="g">A</td></tr>
    <tr><td>Megan Ho</td><td>HVJC</td><td class="g">A</td><td>Nathan Low</td><td>LSJC</td><td class="g">A</td><td>Olivia Seah</td><td>NVJC</td><td class="g">A</td></tr>
    <tr><td>Peter Quek</td><td>EGI</td><td class="g">A</td><td>Rachel Foo</td><td>RSHS</td><td class="g">A</td><td>Samuel Wee</td><td>SBJC</td><td class="g">A</td></tr>
    <tr><td>Tessa Lau</td><td>NVJC</td><td class="g">A</td><td>Victor Pang</td><td>HVJC</td><td class="g">A</td><td>Wendy Chan</td><td>EGI</td><td class="g">A</td></tr>
    <tr><td>Xavier Toh</td><td>LSJC</td><td class="g">A</td><td>Yvonne Kwek</td><td>NVJC</td><td class="g">A</td><td>Zachary Lum</td><td>RSHS</td><td class="g">A</td></tr>
    <tr><td>Amelia Poh</td><td>EGI</td><td class="g">A</td><td>Brandon Yap</td><td>SBJC</td><td class="g">A</td><td>Chloe Heng</td><td>HVJC</td><td class="g">A</td></tr>
    <tr><td>Dylan Soh</td><td>NVJC</td><td class="g">A</td><td>Emily Tang</td><td>EGI</td><td class="g">A</td><td>Gavin Loh</td><td>LSJC</td><td class="g">A</td></tr>
    <tr><td>Hannah Kee</td><td>RSHS</td><td class="g">A</td><td>Ivan Chew</td><td>NVJC</td><td class="g">A</td><td>Jolene Sng</td><td>EGI</td><td class="g">A</td></tr>
    <tr><td>Kevin Liew</td><td>SBJC</td><td class="g">A</td><td>Lydia Oei</td><td>HVJC</td><td class="g">A</td><td>Marcus Ang</td><td>NVJC</td><td class="g">A</td></tr>
    <tr><td>Nicole Phua</td><td>EGI</td><td class="g">A</td><td>Oscar Tee</td><td>LSJC</td><td class="g">A</td><td>Priscilla Yong</td><td>RSHS</td><td class="g">A</td></tr>
    <tr><td>Ryan Kok</td><td>NVJC</td><td class="g">A</td><td>Sabrina Ler</td><td>EGI</td><td class="g">A</td><td>Timothy Hoe</td><td>SBJC</td><td class="g">A</td></tr>
    <tr><td>Ursula Neo</td><td>HVJC</td><td class="g">A</td><td>Vincent Loo</td><td>NVJC</td><td class="g">A</td><td>Whitney Sia</td><td>EGI</td><td class="g">A</td></tr>
    <tr><td>Adeline Ting</td><td>LSJC</td><td class="g">A</td><td>Benjamin Ow</td><td>RSHS</td><td class="g">A</td><td>Cheryl Hui</td><td>NVJC</td><td class="g">A</td></tr>
    <tr><td>Darren Lee</td><td>EGI</td><td class="g">A</td><td>Esther Mok</td><td>SBJC</td><td class="g">A</td><td>Farhan Ali</td><td>HVJC</td><td class="g">A</td></tr>
    <tr><td>Gina Tan</td><td>NVJC</td><td class="g">A</td><td>Howard Lim</td><td>EGI</td><td class="g">A</td><td>Isabel Koh</td><td>LSJC</td><td class="g">A</td></tr>
    <tr><td>Joel Ng</td><td>RSHS</td><td class="g">A</td><td>Kelly Goh</td><td>NVJC</td><td class="g">A</td><td>Lucas Chia</td><td>EGI</td><td class="g">A</td></tr>
    <tr><td>Mabel Teo</td><td>SBJC</td><td class="g">A</td><td>Nigel Ho</td><td>HVJC</td><td class="g">A</td><td>Ong Wei Ling</td><td>NVJC</td><td class="g">A</td></tr>
    <tr><td>Phoebe Yeo</td><td>EGI</td><td class="g">A</td><td>Quentin Sim</td><td>LSJC</td><td class="g">A</td><td>Regina Tay</td><td>RSHS</td><td class="g">A</td></tr>
    <tr><td>Shawn Wong</td><td>NVJC</td><td class="g">A</td><td>Tiffany Chua</td><td>EGI</td><td class="g">A</td><td>Uriel Lau</td><td>SBJC</td><td class="g">A</td></tr>
    <tr><td>Valerie Ong</td><td>HVJC</td><td class="g">A</td><td>Wesley Pang</td><td>NVJC</td><td class="g">A</td><td>Xin Yi Chan</td><td>EGI</td><td class="g">A</td></tr>
    <tr><td>Yong Jie Tan</td><td>LSJC</td><td class="g">A</td><td>Zoe Lim</td><td>RSHS</td><td class="g">A</td><td>Aaron Seah</td><td>NVJC</td><td class="g">A</td></tr>
    <tr><td>Bernice Quah</td><td>EGI</td><td class="g">A</td><td>Calvin Foo</td><td>SBJC</td><td class="g">A</td><td>Denise Wee</td><td>HVJC</td><td class="g">A</td></tr>
  </table>

  <div class="abs testi-tab">Testimonials of Students</div>
  <div class="abs orange-band"></div>
  <div class="abs band-quote" style="left:14px">
    <p>Before I joined this tuition, economics was something I always dreaded, probably because I never understood what was going on in the school. I even scored a U for it at my first test. When I joined the tuition at the beginning of JC, I felt relieved as Mr Koh helped me understand concepts and taught me skills which are relevant to answering essays and case study questions. My reaction towards economics got more positive as I saw real progress.</p>
    <span class="tag"><b>Gwen Lai Shu Ting</b> | Riverside High School</span>
  </div>
  <div class="abs band-quote" style="left:146px">
    <p>As a student who had only gone tuition before in primary 3 and 4, having to go for tuition once again felt strange and awkward. For the whole of JC1, I have never really understood what went on during Econs lectures and tutorials in schools, until I started tuition in JC2. Mr Koh's way of teaching has made Econs a lot easier to understand. He really stayed the whole year with me. Thanks Mr Koh!</p>
    <span class="tag"><b>Ravi Kumar</b> | Eastgate Institution</span>
  </div>
</section>

<section class="page p2">
  <div class="abs photo" style="left:0;top:0;width:278px;height:105px" role="img" aria-label="Group photo of smiling students in matching shirts"></div>
  <div class="abs founder-label">About our Programme <b>Founder</b></div>

  <div class="abs sec-head" style="top:144px">Background</div>
  <div class="abs sec-rule" style="top:151.5px;width:170px"></div>
  <div class="abs body-text" style="left:14px;top:155px;width:170px">
    <p>Mr Adrian Koh is the Programme Founder &amp; Managing Director for Economics At LessonMaple Pte Ltd. He also owns and manages Brightway Education Centre &amp; Clearpath Learning Centre.</p>
  </div>

  <div class="abs sec-head" style="top:183px">Academic Qualifications</div>
  <div class="abs sec-rule" style="top:190.5px;width:170px"></div>
  <div class="abs body-text" style="left:14px;top:194px;width:170px">
    <p>Mr Koh loves and specialises in Economics and he obtained his Bachelor of Arts in Economics from Harbourside University. He is also currently doing his Masters in Applied Economics at Bayfront Management University and he intends to pursue further studies in Economics after his Masters.</p>
  </div>
  <div class="abs photo-grey" style="left:192px;top:146px;width:72px;height:84px" role="img" aria-label="Portrait of the programme founder"></div>

  <div class="abs sec-head" style="top:236px">Teaching Experience</div>
  <div class="abs sec-rule" style="top:243.5px;width:250px"></div>
  <div class="abs body-text" style="left:14px;top:248px;width:170px">
    <p>Mr Koh has established a unique tuition programme under the name of Economics at LessonMaple since 2007. Each year he tutors about 150-200 on average and many of his students were top students in their classes and level for Economics. (read the testimonials!) That means more than a thousand students have gone through Mr Koh's intensive Economics tuition programme!</p>
  </div>
  <div class="abs photo" style="left:188px;top:249px;width:76px;height:42px" role="img" aria-label="Large group photo of students in a classroom"></div>

  <div class="abs sec-head" style="top:296px">Style of Teaching</div>
  <div class="abs sec-rule" style="top:303.5px;width:250px"></div>
  <div class="abs body-text" style="left:14px;top:308px;width:250px">
    <p>Mr Koh is different from other tutors because he employs a mixture of strategies to help the student excel. He thinks that for a student to excel in a subject, he must first be interested in the subject, and that's why Mr Koh tries to make his lessons interesting and relatable to the student. He also looks at the syllabus holistically and reverse engineers the methods to do well for the examination by ensuring that the appropriate right amount of content is covered without compromising on the quality of the learning. Through weekly discussions and looking at real-world problems, Mr Koh also helps his students discover the essential application skills that are required to score that Distinction in the A Levels.</p>
  </div>
</section>

<section class="page p3">
  <div class="abs photo" style="left:0;top:0;width:278px;height:116px" role="img" aria-label="Group photo of students posing in a tuition room"></div>
  <div class="abs testi-label"><b>Testimonials</b> From Students</div>

  <div class="abs tcol" style="left:16px">
    <p>Mr Koh really has all his students' interests at heart. He buys dinner for us, provides us with mini snacks, incentivise us with great rewards; there was also once where he bought me some flu medicine because I was suffering from a bad cold. Thank you Mr Koh!</p>
    <span class="tag"><b>Bryson Tay</b> | Northvale Junior College</span>
    <p>Mr Koh is a very friendly teacher who ensures that his students receive the best. He spends a lot of effort in preparing for lessons such as finding articles that are relevant to the subject and coming up with different ways to help us learn better.</p>
    <span class="tag"><b>Lim Kai Wen</b> | Stonebridge Junior College</span>
    <p>Mr Koh's lessons are very engaging and fun. It's a very different and beneficial tuition style that will definitely benefit students. Content was covered very effectively and thoroughly for each lesson and made easy to understand by Mr Koh's effective teaching methods and anecdotal examples. There is a very comfortable environment here all especially so since there are free refreshments. It has been very enjoyable being in this tuition and Mr Koh is a wonderful tutor.</p>
    <span class="tag"><b>Farah Rahim Aisha</b> | Riverside High School</span>
    <p>Even though I have only been working with Mr Koh for a few months, I have learnt many different skills and specific Singaporean examples that are essential for a good economic grade, but not covered in school classes. Mr Koh also has amazing stories to tell, and I personally am inspired by his 'pilot' story.</p>
    <span class="tag"><b>Darius Fong</b> | Eastgate Institution</span>
  </div>

  <div class="abs tcol" style="left:143px">
    <p>Mr Koh and the tuition centre has greatly improves my quality of work in economics and his knowledge and insights provided during lessons were very valuable to me as an econs student. I was able to perform well in almost all my examinations after attending lessons and this gave me confidence going in A Levels. I would recommend this tuition centre to those in need of help in econs. You can acquire relevant skills in essays and CSQ which I believe will help me pull thru A levels with ease.</p>
    <span class="tag"><b>Jonas Yip</b> | Hillview Junior College</span>
    <p>Mr Koh is a very friendly and approachable tutor who makes economic concepts much easier to understand. His lessons are very well paced and effective and it has helped me increased my school test grades by 3 grades. Tuition at LessonMaple has been fun and very helpful.</p>
    <span class="tag"><b>Calista Wu</b> | Eastgate Institution</span>
    <p>Mr Koh is a very engaging tutor who never fail to pique our interest and curiosity over the economics concepts and the current economy situation. He makes an effort to make interesting analogies to ensure that his students understand certain concepts thoroughly. Kudos!</p>
    <span class="tag"><b>Priya Nair Devi</b> | Eastgate Institution</span>
    <p>I find Mr Koh a committed tutor who does research to provide us with many economics articles and practices for the class. I get much more fruitful practices on essays and case studies during lessons from the group discussions and timed practices that allow me to gauge my understanding knowledge of the topic. Thanks Mr Koh for providing such a unique tuition experience!</p>
    <span class="tag"><b>Natalie Soo Mei Ling</b> | Lakeside Junior College</span>
  </div>

  <div class="abs photo-warm" style="left:16px;top:324px;width:118px;height:50px" role="img" aria-label="Students writing in a lecture room"></div>
  <div class="abs photo-warm" style="left:143px;top:324px;width:119px;height:50px" role="img" aria-label="Class in session with tutor and students"></div>
</section>

<section class="page p4">
  <svg class="abs" style="left:0;top:0" width="278" height="80" viewBox="0 0 278 80">
    <rect width="278" height="26" fill="#f39200"/>
    <polygon points="10,68 268,68 262,76 16,76" fill="#f39200"/>
  </svg>
  <div class="abs photo" style="left:16px;top:16px;width:246px;height:54px" role="img" aria-label="Group photo of students in school uniforms"></div>

  <div class="abs sched-label" style="left:104px;top:101px;width:70px">Class Schedule*</div>
  <table class="abs schedule" style="left:20px">
    <tr><td>JC2 Monday</td><td>5pm</td><td>Westgrove</td></tr>
    <tr><td>JC1 Monday</td><td>7pm</td><td>Westgrove</td></tr>
    <tr><td>JC2 Tuesday</td><td>5:30pm</td><td>Clearwater</td></tr>
    <tr><td>JC1 Tuesday</td><td>7:30pm</td><td>Clearwater</td></tr>
    <tr><td>JC1 Wednesday</td><td>6pm</td><td>Eastbay</td></tr>
    <tr><td>JC2 Wednesday</td><td>8pm</td><td>Eastbay #</td></tr>
    <tr><td>JC2 Thursday</td><td>5:30pm</td><td>Hillcrest</td></tr>
    <tr><td>JC1 Thursday</td><td>7:30pm</td><td>Hillcrest</td></tr>
  </table>
  <table class="abs schedule" style="left:142px">
    <tr><td>JC2 Saturday</td><td>10am</td><td>Hillcrest</td></tr>
    <tr><td>JC2 Saturday</td><td>12pm</td><td>Hillcrest</td></tr>
    <tr><td>JC1 Saturday</td><td>2pm</td><td>Hillcrest</td></tr>
    <tr><td>JC2 Saturday</td><td>4pm</td><td>Hillcrest</td></tr>
    <tr><td>JC1 Sunday</td><td>10am</td><td>Hillcrest</td></tr>
    <tr><td>JC1 Sunday</td><td>12pm</td><td>Hillcrest</td></tr>
    <tr><td>JC2 Sunday</td><td>2pm</td><td>Hillcrest</td></tr>
    <tr><td>JC1 Sunday</td><td>4pm</td><td>Hillcrest</td></tr>
  </table>
  <div class="abs" style="left:0;top:182px;width:278px;text-align:center;font-size:3.6px">*MOST Classes are already full, call/SMS/Whatsapp us at 80001234 to confirm available timings.</div>

  <div class="abs loc-bar">Our Locations</div>
  <div class="abs loc-box">
    <div class="abs loc" style="left:10px;top:5px"><h3>Hillcrest:</h3>Blk 120 Hillcrest Ave 3 #02-415,<br>S681120,<br>2 minutes walk from Hillcrest MRT</div>
    <div class="abs loc" style="left:108px;top:5px"><h3>Eastbay:</h3>Blk 48 Eastbay North St 2 #01-22<br>(2nd storey),<br>S460048)<br>7 minutes walk from Eastbay MRT</div>
    <div class="abs loc" style="left:10px;top:40px"><h3>Clearwater:</h3>Blk 215 Clearwater Ave 4 #01-109,<br>S120215,<br>5 min bus ride from Clearwater MRT</div>
    <div class="abs loc" style="left:108px;top:40px"><h3>Westgrove:</h3>Westgrove Drive (along Westgrove<br>Avenue 5, opposite petrol station)<br>5 minutes bus ride from LJC / RSHS</div>
  </div>

  <div class="abs fees-label" style="left:100px;top:305px;width:78px">Fees &amp; Promotions</div>
  <div class="abs fees">
    $295 per month – JC2s<br>
    $280 per month – JC1s (early bird promotion)<br>
    Sign up with a friend(s) to enjoy $20 off monthly fees.
  </div>
  <div class="abs contact">Sign up now / Contact Us<br>Text/Call/Whatsapp us at <b>80001234</b></div>
</section>

</body>
</html>
```